Travel Group 'Lydgate Group' needs a new business card design

Lydgate Group is a diverse business specialising in bespoke, tailor made holidays to suit all budgets and we are specialists in planning exciting day/short trips to suit all markets. Our target market is very varied going from the corporate client and as well as people in the community who simply want to experience something special.
We are looking for a card design that will encourage people to look at our websites and social media platforms and to see for themselves the different facets to our business. It is essential that the card has social media icons for Facebook, Twitter and Instagram. We are looking for a card with a blank background with no pictures and for the front side to have the attached Lydgate logo. The card should have similar colour scheme to the attached Lydgate logo.
The card must have the following information on one side:
Maud Penrose
Business Development Manager
maudpenrose@lydgatevoyages.example
Lydgate Group, 87 Quarry Lane
Kilwinning, Ayrshire, Scotland KA19 4TN
+44 (0)1294 730182
And then the card must have the following on the second side:
(Lydgate logo)
(social media icons)
www.lydgatevoyages.example
www.lydgateoutings.example
Target Market(s)
Our target market is very varied going from the corporate client and as well as people in the community who simply want to experience something special.
Industry/Entity Type
Business
Contact Information for Business Card
Maud Penrose
+44 (0)1294 730182
(Lydgate logo)
(social media icons)
www.lydgatevoyages.example
www.lydgateoutings.example
Requirements
Must have
- It is essential that the card has social media icons for Facebook, Twitter & Instagram.
Should not have
- Should not have any images other than Lydgate logo.

```html
<!DOCTYPE html>
<html lang="en">
<head>
<meta charset="utf-8">
<title>Lydgate Group – Business Card</title>
<link rel="stylesheet" href="https://fonts.googleapis.com/css2?family=Bebas+Neue&family=Open+Sans:wght@400;600;700&display=swap">
<style>
  :root {
    --backdrop: #e8e5e1;
    --navy: #272261;
    --deep-indigo: #2a2766;
    --magenta: #a51f7d;
    --white: #ffffff;
    --ink-grey: #4a4a4f;
    --rule-grey: #8a8a90;
  }
  * { margin: 0; padding: 0; box-sizing: border-box; }
  html, body {
    width: 1200px; height: 1000px; overflow: hidden;
    background: var(--backdrop);
    font-family: "Open Sans", Arial, sans-serif;
  }
  .canvas { position: relative; width: 1200px; height: 1000px; }

  .card {
    position: absolute; left: 266px; width: 666px; height: 397px;
    box-shadow: 0 2px 6px rgba(0,0,0,0.18);
  }
  .card-front {
    top: 74px;
    background: radial-gradient(ellipse 60% 70% at 50% 48%, var(--magenta) 0%, #6a2275 45%, var(--deep-indigo) 85%);
    color: var(--white);
  }
  .card-back { top: 533px; background: var(--white); }

  .brand-name {
    position: absolute; left: 0; right: 0; top: 212px;
    text-align: center;
    font-weight: 600; font-size: 44px; letter-spacing: 4px;
    color: var(--white);
  }
  .social-row {
    position: absolute; left: 0; right: 0; top: 318px;
    display: flex; justify-content: center; gap: 6px;
  }
  .social-dot { width: 18px; height: 18px; border-radius: 50%; background: var(--white); }
  .web-links {
    position: absolute; left: 0; right: 0; top: 347px;
    text-align: center; font-size: 16px; color: var(--white);
  }
  .web-links .divider { margin: 0 6px; }

  .holder {
    position: absolute; right: 372px; top: 168px; text-align: right;
  }
  .holder-name {
    font-family: "Bebas Neue", Impact, sans-serif;
    font-size: 40px; line-height: 38px; color: var(--navy); letter-spacing: 0.5px;
  }
  .holder-role { font-size: 16px; color: var(--ink-grey); line-height: 22px; }
  .split-rule {
    position: absolute; left: 318px; top: 172px; width: 1.5px; height: 50px;
    background: var(--rule-grey);
  }
  .contact-list {
    position: absolute; left: 343px; top: 173px;
    list-style: none; font-size: 15px; color: var(--ink-grey); line-height: 25px;
  }
  .contact-list li { display: flex; align-items: center; gap: 8px; }
  .contact-list svg { fill: var(--navy); flex: none; }
  .address {
    position: absolute; left: 0; right: 0; top: 347px;
    display: flex; justify-content: center; align-items: center; gap: 7px;
    font-size: 16px; color: var(--ink-grey);
  }
  .address svg { fill: var(--navy); }
  .address strong { color: var(--navy); font-weight: 700; }
</style>
</head>
<body>
<main class="canvas">
  <section class="card card-front">
    <div class="brand-name">LYDGATE</div>
    <div class="social-row" aria-label="Social media">
      <span class="social-dot"></span>
      <span class="social-dot"></span>
      <span class="social-dot"></span>
    </div>
    <p class="web-links">www.lydgatevoyages.example<span class="divider">|</span>www.lydgateoutings.example</p>
  </section>

  <section class="card card-back">
    <div class="holder">
      <h1 class="holder-name">MAUD PENROSE</h1>
      <p class="holder-role">Business Development</p>
    </div>
    <div class="split-rule"></div>
    <ul class="contact-list">
      <li>
        <svg width="14" height="12" viewBox="0 0 14 12" aria-hidden="true"><path d="M1 3c0-1.5 2.5-2.5 6-2.5S13 1.5 13 3v1.5h-3V3H4v1.5H1z"/><rect x="2.5" y="5.5" width="9" height="6" rx="1"/></svg>
        +44 (0)1294 730182
      </li>
      <li>
        <svg width="14" height="11" viewBox="0 0 14 11" aria-hidden="true"><path d="M0 0h14v11H0z M1.2 1.2 7 6l5.8-4.8" /><path d="M1.5 1.5 7 6l5.5-4.5" stroke="#fff" stroke-width="1.2" fill="none"/></svg>
        maudpenrose@lydgatevoyages.example
      </li>
    </ul>
    <p class="address">
      <svg width="13" height="18" viewBox="0 0 13 18" aria-hidden="true"><path d="M6.5 0A6.5 6.5 0 0 0 0 6.5C0 11 6.5 18 6.5 18S13 11 13 6.5A6.5 6.5 0 0 0 6.5 0zm0 9a2.5 2.5 0 1 1 0-5 2.5 2.5 0 0 1 0 5z"/></svg>
      <span><strong>Lydgate Group</strong> 87 Quarry Lane Kilwinning, Ayrshire, Scotland KA19 4TN</span>
    </p>
  </section>
</main>
</body>
</html>
```